Business Card design for a mobile solutions company

- we are a mobile telecommunications company focusing on mobile content and solutions
- we are based in Malaysia however operate a regional business
- attached is our company logo and current business card design
- please try to incorporate the "cubes" into the design

our company philosophy is dynamic and outgoing. we are a lean team of less than 50, but we have strong roots in the mobile industry in Asia and we like to challenge ourselves by taking on larger projects.

we love joint ventures and working with partners to find the right solutions for our clients

*please feel free to modify our logo (typeface etc)
**we would like to keep the 3 cube design for the logo, but I would love to see different versions of it
Updates

some of the designs are great and I think our logo (especially the typeface used for the words) doesn't look good. please feel free to update the logo but try to keep the cubes, you are free to modify the cubes and update them.

Reason: looking for more design please

Industry/Entity Type

Telecommunications

Font styles to use
Sans Serif

```html
<!DOCTYPE html>
<html lang="en">
<head>
<meta charset="utf-8">
<title>Kite Harbor – Business Card</title>
<link href="https://fonts.googleapis.com/css2?family=Open+Sans:wght@400;700&display=swap" rel="stylesheet">
<style>
  :root {
    --paper: #fbfcfc;
    --band-grey: #ebeceb;
    --ink: #111111;
    --bar-black: #0e0e0e;
    --white: #ffffff;
    --magenta: #ff00ff;
    --cyan: #00f6ff;
    --lime: #66ff00;
    --mark-dark: #3d3939;
  }
  html, body {
    margin: 0;
    padding: 0;
    width: 1200px;
    height: 720px;
    overflow: hidden;
    background: var(--white);
    font-family: "Open Sans", sans-serif;
  }
  .card {
    position: relative;
    width: 1200px;
    height: 720px;
    background: var(--paper);
    overflow: hidden;
  }
  .name-band {
    position: absolute;
    left: 0;
    top: 180px;
    width: 739px;
    height: 87px;
    background: var(--band-grey);
  }
  .name-band-end {
    position: absolute;
    left: 1099px;
    top: 180px;
    width: 101px;
    height: 87px;
    background: var(--band-grey);
  }
  .person-name {
    position: absolute;
    left: 103px;
    top: 198px;
    margin: 0;
    font-size: 38px;
    font-weight: 700;
    color: var(--ink);
    letter-spacing: 0.5px;
    line-height: 50px;
  }
  .person-title {
    position: absolute;
    left: 476px;
    top: 208px;
    margin: 0;
    font-size: 21px;
    font-weight: 400;
    color: var(--ink);
    line-height: 28px;
  }
  .brand-mark {
    position: absolute;
    left: 782px;
    top: 110px;
    width: 290px;
    height: 256px;
    display: flex;
    flex-direction: column;
    align-items: center;
    justify-content: center;
    gap: 18px;
  }
  .brand-mark-square {
    width: 56px;
    height: 56px;
    background: var(--cyan);
  }
  .brand-mark-name {
    font-size: 34px;
    font-weight: 700;
    color: var(--mark-dark);
    letter-spacing: 0.5px;
  }
  .company-bar {
    position: absolute;
    left: 0;
    top: 406px;
    width: 1200px;
    height: 103px;
    background: var(--bar-black);
  }
  .company-name {
    position: absolute;
    left: 0;
    width: 1238px;
    top: 0;
    margin: 0;
    text-align: center;
    line-height: 103px;
    font-size: 47px;
    font-weight: 700;
    color: var(--white);
  }
  .contact-tile {
    position: absolute;
    top: 516px;
    height: 204px;
    color: var(--white);
    text-align: center;
    font-size: 22px;
    line-height: 31px;
  }
  .contact-tile svg {
    display: block;
    margin: 11px auto 0;
  }
  .contact-tile p { margin: 0; }
  .tile-address { left: 0; width: 410px; background: var(--magenta); }
  .tile-phone { left: 416px; width: 369px; background: var(--cyan); }
  .tile-email { left: 791px; width: 409px; background: var(--lime); }
  .tile-address p { margin-top: 16px; }
  .tile-phone p { margin-top: 14px; text-align: left; padding-left: 74px; }
  .tile-email p { margin-top: 24px; }
</style>
</head>
<body>
  <main class="card">
    <div class="name-band"></div>
    <div class="name-band-end"></div>
    <h1 class="person-name">MAREN LOH</h1>
    <p class="person-title">chief marketing officer</p>

    <div class="brand-mark">
      <span class="brand-mark-square"></span>
      <span class="brand-mark-name">KITE HARBOR</span>
    </div>

    <div class="company-bar">
      <h2 class="company-name">KITE HARBOR</h2>
    </div>

    <section class="contact-tile tile-address">
      <svg width="34" height="44" viewBox="0 0 34 44" aria-hidden="true">
        <path d="M17 0C7.6 0 0 7.4 0 16.6 0 28 17 44 17 44s17-16 17-27.4C34 7.4 26.4 0 17 0z" fill="#fff"/>
        <circle cx="17" cy="16" r="6" fill="var(--magenta)"/>
      </svg>
      <p>Lorong Cempaka No 12,<br>Taman Seri,<br>Kuala Lumpur 59100</p>
    </section>

    <section class="contact-tile tile-phone">
      <svg width="42" height="42" viewBox="0 0 42 42" aria-hidden="true">
        <path d="M9 2l7 8-4 5c2 6 7 11 13 14l5-4 8 7-5 7C18 38 3 23 2 7z" fill="#fff"/>
      </svg>
      <p>+ 60 3 555 0192<br>+ 62 855 0004172</p>
    </section>

    <section class="contact-tile tile-email">
      <svg width="32" height="40" viewBox="0 0 32 40" aria-hidden="true">
        <path d="M2 14L16 2l14 12v24H2z" fill="#fff"/>
        <path d="M2 38l14-13 14 13M2 16l14 11 14-11" fill="none" stroke="var(--lime)" stroke-width="2.5"/>
      </svg>
      <p>maren@kiteharbor.com.my</p>
    </section>
  </main>
</body>
</html>
```